Fun, Clean Business Card For Family Focused Travel Agency

I need a business card using specific colors and fonts as in the uploaded files. Ideally, I would like a large image of the logo on the back and all the contact info on the front. Maybe the stars/dots somewhere in a flowy form.

I do want it the contact information to be clear and easy to read. I don't want it to look too busy. Maybe even a bit minimalist.

I plan or ordering the ROUNDED CORNER business cards from Cardwell Press, so please consider that in your design.

Target Market(s)

Families with children, couples, groups of friends

Contact Information for Business Card

Marla Quent, Owner
Marla@TidewayTrips.example
Cell Phone Number 555-218-6034
Office Phone Number 555-647-1295
Specializing in Fablecrest destinations, Goldmere Parkside Resort, Cruises and All-Inclusive Vacations.

Nice but not required:
www.TidewayTrips.example
Facebook, Instagram, Twitter icons with username: TidewayTrips

Font styles to use
Sans Serif

Requirements
Must have
• Please try to use the colors from the logo as much as possible. I understand lighter shades/colors may be needed for some things.
Should not have
• NO SERIF FONTS. That is really the only thing I do not want at all

```html
<!DOCTYPE html>
<html lang="en">
<head>
<meta charset="utf-8">
<title>Tideway Trips – Business Card</title>
<link href="https://fonts.googleapis.com/css2?family=Fira+Sans:ital,wght@0,400;0,500;0,600;1,500&display=swap" rel="stylesheet">
<style>
  :root {
    --stage: #2b2c2f;
    --navy: #0b1030;
    --navy-soft: #141a3d;
    --teal: #1fb59a;
    --white: #ffffff;
    --rule: #5b6079;
  }
  html, body {
    margin: 0;
    padding: 0;
    width: 1200px;
    height: 1108px;
    overflow: hidden;
    background: var(--stage);
    font-family: "Fira Sans", sans-serif;
  }
  .canvas {
    position: relative;
    width: 1200px;
    height: 1108px;
    display: flex;
    justify-content: center;
    align-items: center;
    gap: 60px;
  }
  .card {
    position: relative;
    width: 420px;
    height: 700px;
    border-radius: 26px;
    background: var(--navy);
    overflow: hidden;
    box-shadow: 0 18px 40px rgba(0,0,0,0.45);
    color: var(--white);
  }
  /* front */
  .brand {
    position: absolute;
    top: 200px;
    left: 0;
    right: 0;
    display: flex;
    justify-content: center;
    align-items: center;
    gap: 14px;
  }
  .brand-dot {
    width: 22px;
    height: 22px;
    border-radius: 50%;
    background: var(--teal);
    flex: none;
  }
  .brand-name {
    font-family: "Fira Sans", sans-serif;
    font-weight: 600;
    font-size: 44px;
    color: var(--white);
    letter-spacing: 0.5px;
    white-space: nowrap;
  }
  .identity {
    position: absolute;
    top: 410px;
    left: 0;
    right: 0;
    text-align: center;
  }
  .person-name {
    font-family: "Fira Sans", sans-serif;
    font-style: italic;
    font-weight: 500;
    font-size: 36px;
    color: var(--teal);
    line-height: 1.1;
  }
  .person-role {
    font-size: 19px;
    margin-top: 4px;
  }
  .rule {
    width: 210px;
    height: 1px;
    background: var(--rule);
    margin: 10px auto 14px;
  }
  .contact {
    list-style: none;
    margin: 0;
    padding: 0;
    font-size: 19px;
    line-height: 1.5;
    white-space: nowrap;
  }
  .contact .label {
    color: var(--teal);
    font-weight: 500;
    margin-right: 6px;
  }
  /* back */
  .pattern {
    position: absolute;
    inset: 0;
    background: radial-gradient(ellipse at 50% 35%, var(--navy-soft) 0%, var(--navy) 75%);
  }
  .back-brand {
    position: absolute;
    top: 450px;
    left: 0;
    right: 0;
    display: flex;
    justify-content: center;
    align-items: center;
    gap: 10px;
  }
  .back-brand .brand-dot { width: 14px; height: 14px; }
  .back-brand .brand-name { font-size: 24px; }
  .specialties {
    position: absolute;
    top: 530px;
    left: 0;
    right: 0;
    text-align: center;
    font-size: 20px;
    line-height: 1.35;
    margin: 0;
  }
</style>
</head>
<body>
<main class="canvas">
  <section class="card card-front">
    <div class="brand">
      <span class="brand-dot"></span>
      <span class="brand-name">Tideway Trips</span>
    </div>
    <div class="identity">
      <div class="person-name">Marla Quent</div>
      <div class="person-role">Owner</div>
      <div class="rule"></div>
      <ul class="contact">
        <li><span class="label">P:</span>555-218-6034</li>
        <li><span class="label">M:</span>555-647-1295</li>
        <li><span class="label">E:</span>Marla@TidewayTrips.example</li>
        <li><span class="label">W:</span>www.TidewayTrips.example</li>
      </ul>
    </div>
  </section>

  <section class="card card-back">
    <div class="pattern" role="img" aria-label="Faint repeating pattern of the brand symbol"></div>
    <div class="back-brand">
      <span class="brand-dot"></span>
      <span class="brand-name">Tideway Trips</span>
    </div>
    <p class="specialties">
      Specializing in Fablecrest destinations<br>
      Goldmere Parkside Resort<br>
      Cruises and All-Inclusive Vacations
    </p>
  </section>
</main>
</body>
</html>
```